Farming Post Card

We are both a real estate company and an estate specialist. We need a 'Just Sold' on one side and the other side would advertise our estate specialist business

Target Market(s)

Residents planning to sell house

Industry/Entity Type

Real Estate

Requirements
Must have
• Please visit our website www.drobenko.com. One side must advertise our Auction House business and the other side is our 'Just Sold' advertisement. We are both a realtor and a estate specialist.

```html
<!DOCTYPE html>
<html lang="en">
<head>
<meta charset="utf-8">
<title>Drobenko Postcard</title>
<link href="https://fonts.googleapis.com/css2?family=Anton&family=Bebas+Neue&family=Lato:wght@400;700&family=Oswald:wght@300;400;700&display=swap" rel="stylesheet">
<style>
:root{
  --blue:#2b39a6;
  --blue-dark:#1f2b8a;
  --red:#e0202a;
  --ink:#222;
  --grey:#3a3a3a;
  --paper:#ffffff;
  --bg:#e6e6e6;
}
*{box-sizing:border-box;margin:0;padding:0}
html,body{width:1200px;height:1200px;overflow:hidden;background:var(--bg);font-family:'Lato',sans-serif}
.canvas{width:1200px;height:1200px;display:flex;flex-direction:column;align-items:center;justify-content:center;gap:30px}
.card{position:relative;width:840px;height:560px;background:var(--paper);overflow:hidden;box-shadow:0 4px 14px rgba(0,0,0,.18)}

/* back side */
.bio-panel{position:absolute;left:0;top:0;width:545px;height:400px;background:var(--blue);color:#fff;padding:36px 34px 0 40px}
.bio-photo{position:absolute;left:40px;top:64px;width:132px;height:124px;border:5px solid #fff;background:linear-gradient(135deg,#c9c4bd,#8d8a86 55%,#5b5f6b)}
.bio-title{margin-left:232px;font-family:'Bebas Neue',sans-serif;font-size:22px;letter-spacing:.3px}
.bio-lead{margin-left:232px;margin-top:8px;font-size:12.2px;line-height:15.2px;text-align:justify}
.bio-body{margin-top:4px;font-size:12.2px;line-height:15.2px;text-align:justify}
.contact{position:absolute;left:0;top:400px;width:545px;height:160px}
.agent-photo{position:absolute;left:60px;top:20px;width:140px;height:140px;background:linear-gradient(180deg,#d5d9df,#2a2f3c 70%)}
.contact-rule{position:absolute;left:258px;top:28px;width:2px;height:108px;background:var(--blue)}
.contact-name{position:absolute;left:272px;top:22px;font-family:'Oswald',sans-serif;font-weight:300;font-size:24px;color:var(--blue)}
.contact-list{position:absolute;left:272px;top:62px;list-style:none;font-size:11.5px;color:var(--ink);line-height:17px}
.contact-list li{display:flex;align-items:flex-start;gap:7px}
.contact-list svg{flex:none;margin-top:3px}
.divider{position:absolute;left:552px;top:0;width:5px;height:560px;background:#111}
.stamp-box{position:absolute;left:730px;top:14px;width:74px;height:86px;border:1.5px solid #111}
.address-line{position:absolute;left:590px;width:200px;height:1.5px;background:#111}

/* front side */
.house-photo{position:absolute;left:0;top:0;width:402px;height:560px;background:linear-gradient(180deg,#a9c98a 0%,#6f9c55 35%,#c9bfa2 55%,#8aa56a 75%,#4f8a3a 100%)}
.sold-panel{position:absolute;left:402px;top:0;width:438px;height:560px}
.brand{position:absolute;left:60px;top:24px;display:flex;align-items:center;gap:10px}
.brand-mark{width:26px;height:26px;background:var(--blue)}
.brand-name{font-family:'Lato',sans-serif;font-weight:700;font-size:14px;letter-spacing:1px;color:var(--blue);line-height:16px}
.brand-tag{font-family:'Lato',sans-serif;font-weight:700;font-size:7px;letter-spacing:.5px;color:var(--blue)}
.sold-band{position:absolute;left:0;top:60px}
.sold-word{position:absolute;left:0;width:438px;top:122px;text-align:center;font-family:'Anton',sans-serif;font-size:104px;line-height:1;color:var(--red);-webkit-text-stroke:3px #fff;paint-order:stroke fill;letter-spacing:1px}
.pitch{position:absolute;left:160px;top:340px;padding-left:14px;border-left:2px solid var(--blue)}
.pitch-line{font-family:'Oswald',sans-serif;line-height:1.05;display:block}
.pitch-1{font-size:30px;font-weight:300;color:var(--blue)}
.pitch-2{font-size:28px;font-weight:700;color:var(--grey);letter-spacing:-.5px}
.pitch-3{font-size:21px;font-weight:400;color:var(--blue);font-family:'Lato',sans-serif;letter-spacing:.5px}
.pitch-4{font-size:21px;font-weight:300;color:var(--grey);font-family:'Oswald',sans-serif;letter-spacing:1px}
.web-strip{position:absolute;left:520px;bottom:0;width:320px;height:36px;background:var(--blue);color:#fff;font-size:11px;font-weight:700;display:flex;align-items:center;justify-content:flex-end;padding-right:24px}
.front-agent{position:absolute;left:275px;top:300px;width:250px;height:260px;background:linear-gradient(180deg,#d9dde3 0%,#1f2434 62%)}
</style>
</head>
<body>
<main class="canvas">

  <section class="card card-back" aria-label="Postcard back">
    <div class="bio-panel">
      <div class="bio-photo" role="img" aria-label="Photo of three businesswomen holding cash at a desk"></div>
      <h2 class="bio-title">Victor Drobenko, Realtor</h2>
      <p class="bio-lead">Victor Drobenko brings over 30 years of sales and marketing experience to Harbor Lane Real Estate. His network of 35,000 constant contact emails, intensive print and social marketing campaigns, and experience as a professional negotiator makes him a solid choice to represent your property. He also has a</p>
      <p class="bio-body">full network of Chinese investors looking for property in your area, and his sales team includes fluent Mandarin and Cantonese speakers. Owner of Drobenko Auctioneers, he is bonded by the State of California. As a benefit for a potential seller of their home, Victor can also offer his clients exposure to over 140 million online bidders to sell the personal property through the auction company. He has served on Regional Governing Boards and has the confidence of government agencies selling property on behalf of their clients. Victor looks forward to selling your property in a timely manner and achieving the highest price possible.</p>
    </div>
    <div class="contact">
      <div class="agent-photo" role="img" aria-label="Portrait of the realtor in a dark suit"></div>
      <div class="contact-rule"></div>
      <h3 class="contact-name">Victor Drobenko</h3>
      <ul class="contact-list">
        <li><svg width="9" height="9" viewBox="0 0 10 10"><path d="M2 0l2 2-1 2 3 3 2-1 2 2-2 2C4 10 0 6 0 2z" fill="#2b39a6"/></svg>(408) 555-0142</li>
        <li><svg width="10" height="8" viewBox="0 0 10 8"><rect x=".5" y=".5" width="9" height="7" fill="none" stroke="#2b39a6"/><path d="M.5 .5l4.5 4 4.5-4" fill="none" stroke="#2b39a6"/></svg>victor@harborlane.com</li>
        <li><svg width="8" height="11" viewBox="0 0 8 11"><path d="M4 11S0 6 0 4a4 4 0 018 0c0 2-4 7-4 7z" fill="#2b39a6"/><circle cx="4" cy="4" r="1.5" fill="#fff"/></svg>2400 Cedar Ridge Road Suite 210<br>Oak Valley, CA 95000</li>
      </ul>
    </div>
    <div class="divider"></div>
    <div class="stamp-box"></div>
    <div class="address-line" style="top:300px"></div>
    <div class="address-line" style="top:335px"></div>
    <div class="address-line" style="top:370px"></div>
  </section>

  <section class="card card-front" aria-label="Postcard front">
    <div class="house-photo" role="img" aria-label="Photo of a cream two-storey house with porch, trees and flower garden"></div>
    <div class="sold-panel">
      <div class="brand">
        <span class="brand-mark"></span>
        <div>
          <div class="brand-name">DROBENKO AUCTIONEERS</div>
          <div class="brand-tag">Real Estate | Auctions | Appraisals</div>
        </div>
      </div>
      <svg class="sold-band" width="438" height="240" viewBox="0 0 438 240">
        <polygon points="0,8 219,36 438,8 438,18 219,46 0,18" fill="#3a3a3a"/>
        <polygon points="0,18 219,46 438,18 438,222 219,200 0,222" fill="#2b39a6"/>
        <polygon points="0,222 219,200 438,222 438,232 219,210 0,232" fill="#3a3a3a"/>
      </svg>
      <div class="sold-word">SOLD !</div>
      <div class="pitch">
        <span class="pitch-line pitch-1">LIST WITH VICTOR &amp;</span>
        <span class="pitch-line pitch-2">GET YOUR PROPERTY</span>
        <span class="pitch-line pitch-3">COMPREHENSIVE</span>
        <span class="pitch-line pitch-4">ESTATE SERVICES</span>
      </div>
    </div>
    <div class="web-strip">www.drobenko.com</div>
    <div class="front-agent" role="img" aria-label="Portrait of the realtor in a dark suit and blue tie"></div>
  </section>

</main>
</body>
</html>
```